WP website design (Stoneridge)

We need a wordpress design that will incorporate a professional color scheme with company logo in a clean layout. The design needs to consider that this will be developed on a responsive theme. Colors are either 1) green of the logo, and tan and an accent color maybe black; or other highlight for the logo that without the green. Client wants a 'modern' look.

Industry/Entity Type

It Company

Number of Pages Required

1 page

Font styles to use
Serif
Sans Serif

Requirements
Must have
• Navigation - 1) Home 2) Real Estate 3) Auction Calendar 4) About Us 5) Terms & Conditions 6) FAQ 7) Contact Us
• Site will have full width slideshow 960px. Use stock real estate photo. Header will have logo (attached) and contact info:
• Main Office:
• 417 E Hazel Rd
• Marston, VA 24873
• (800) 555-0173
• (540) 555-0148
• Dunmore Office:
• 318 1/2 S. Mill Rd.
• Dunmore, WV 24987
• (304) 555-0192
• Widgets - in the sidebar or footer of site - email signup form; featured auctions; testimonials; Facebook and RSS social icons; link to broker participation form; News and Events Blog.
Nice to have
• use of dropdown menus styling displayed - 1) Current Auctions & 2) Past Auctions under the Auction Calendar link

```html
<!DOCTYPE html>
<html lang="en">
<head>
<meta charset="utf-8">
<title>Stoneridge Real Estate &amp; Auction</title>
<link href="https://fonts.googleapis.com/css2?family=Lato:wght@400;700;900&family=Oswald:wght@500&display=swap" rel="stylesheet">
<style>
:root{
  --green:#9bbd1e;
  --green-dark:#7f9e12;
  --green-light:#b5d13a;
  --black:#111111;
  --ink:#2b2b2b;
  --muted:#666666;
  --grey-band:#e7e7e7;
  --card:#e3e3e3;
  --white:#ffffff;
  --orange:#d8430f;
  --yellow:#f6c12a;
  --footer-text:#bdbdbd;
}
*{box-sizing:border-box;margin:0;padding:0}
html,body{width:1200px;height:2609px;overflow:hidden;background:var(--white)}
body{position:relative;font-family:'Lato',Arial,sans-serif;color:var(--ink)}
.abs{position:absolute}

/* header */
.site-header{left:0;top:0;width:1200px;height:139px;background:var(--white)}
.brand{left:74px;top:22px;display:flex;align-items:center;gap:14px}
.brand-dot{width:60px;height:60px;border-radius:50%;background:var(--green)}
.brand-name{font-weight:900;font-size:38px;color:var(--black);letter-spacing:.5px}
.social{display:flex;gap:6px}
.social span{display:block;width:28px;height:28px;border-radius:50%;background:#c9c9c9}
.header-social{left:1036px;top:12px}
.office-contact{top:70px}
.office-contact .label{font-size:13px;color:#888;letter-spacing:.5px;text-transform:uppercase}
.office-contact .phone{font-size:23px;font-weight:700;color:var(--black);margin-top:2px}
.contact-va{left:793px}
.contact-wv{left:985px}
.phone-icon{left:746px;top:78px}
.header-divider{left:958px;top:72px;width:1px;height:42px;background:#cccccc}

/* nav */
.main-nav{left:0;top:139px;width:1200px;height:40px;background:var(--green)}
.main-nav ul{list-style:none;display:flex;margin-left:80px;height:40px;align-items:center;gap:33px}
.main-nav li{font-size:14px;font-weight:700;color:var(--white);text-transform:uppercase;letter-spacing:.3px;position:relative}
.main-nav li.active{color:var(--black)}
.main-nav li.active::before{content:"";position:absolute;left:-6px;right:-6px;top:-13px;height:4px;background:var(--black)}

/* hero */
.hero{left:0;top:179px;width:1200px;height:534px;background:linear-gradient(180deg,#dfeaf2 0%,#b9d0e2 28%,#7da24a 46%,#5b8a2c 66%,#3f6a1f 84%,#2f5318 100%)}
.hero-arrow{top:410px}
.arrow-left{left:32px}
.arrow-right{left:1140px}

/* welcome */
.welcome{left:0;top:713px;width:1200px;height:248px;background:var(--grey-band);text-align:center}
.section-title{font-size:22px;font-weight:700;color:var(--black);text-transform:uppercase;letter-spacing:.3px}
.welcome .section-title{margin-top:50px}
.welcome p{width:1060px;margin:24px auto 0;font-size:13px;line-height:21px;color:#555}

/* auctions */
.auctions{left:0;top:961px;width:1200px;height:540px}
.auctions .section-title{position:absolute;top:34px;width:100%;text-align:center}
.auction-card{top:91px;width:238px;height:427px;background:var(--card);text-align:center}
.auction-card .flyer{margin:16px auto 0;width:206px;height:200px;background:var(--white);display:flex;align-items:center;justify-content:center}
.auction-card .flyer div{width:150px;height:160px}
.flyer-bw{background:linear-gradient(180deg,#3a3a3a,#8a8a8a 40%,#cfcfcf)}
.flyer-green{background:linear-gradient(180deg,#1e4d2b,#3d7a3a 50%,#86a85a)}
.flyer-red{background:linear-gradient(180deg,#e8d34a,#d9442a 45%,#e8c86a)}
.auction-card h3{margin:24px 22px 0;font-size:13px;font-weight:700;color:var(--black);line-height:17px;min-height:34px}
.auction-card p{margin-top:10px;font-size:12px;line-height:18px;color:#444}
.btn-details{display:inline-block;margin-top:16px;width:114px;height:40px;line-height:40px;border-radius:20px;background:var(--green);color:var(--white);font-size:13px;font-weight:700}

/* testimonials */
.testimonials{left:74px;top:1522px;width:602px;text-align:center}
.testimonials .section-title{margin-top:12px}
.quote-mark{display:block;margin:24px auto 0}
.testimonials blockquote{margin:22px 20px 0;font-size:14px;line-height:22px;color:#333}
.client{display:flex;justify-content:center;align-items:center;gap:10px;margin-top:16px}
.client-photo{width:44px;height:44px;border-radius:50%;background:linear-gradient(180deg,#8a5a44,#d9b49a)}
.client-meta{text-align:left}
.client-meta strong{display:block;font-size:13px;color:#333}
.client-meta span{font-size:12px;color:#888}
.dots{display:flex;justify-content:center;gap:6px;margin-top:22px}
.dots span{width:11px;height:11px;border-radius:50%;background:#d4d4d4}
.dots span.on{background:var(--green)}

/* alerts */
.alerts{left:74px;top:1882px;width:602px;height:194px;background:var(--green);text-align:center}
.alerts h2{margin-top:30px;font-size:23px;font-weight:700;color:var(--black);text-transform:uppercase}
.alerts p{margin-top:6px;font-size:13px;color:var(--black)}
.alerts form{display:flex;width:424px;margin:18px auto 0;height:44px}
.alerts .field{flex:1;background:var(--white);font-size:13px;color:#666;text-align:left;line-height:44px;padding-left:16px;border:1px solid #ddd}
.alerts .subscribe{width:102px;background:var(--black);color:var(--white);font-size:13px;font-weight:700;line-height:44px}

/* question form */
.question{left:709px;top:1522px;width:418px;height:554px;background:var(--black);padding:0 28px}
.question h2{margin-top:24px;text-align:center;font-size:24px;font-weight:700;color:var(--white);text-transform:uppercase}
.question .rule{width:80px;height:2px;background:#888;margin:12px auto 0}
.question label{display:block;margin-top:18px;font-size:13px;font-weight:700;color:var(--white)}
.question .input{margin-top:8px;height:42px;background:var(--white);border-radius:3px;font-size:13px;color:#666;line-height:42px;padding-left:10px}
.question .pair{display:flex;gap:10px}
.question .pair .input{flex:1}
.question .textarea{margin-top:8px;height:104px;background:var(--white);border-radius:3px}
.question .submit{margin-top:16px;height:54px;border-radius:4px;background:linear-gradient(180deg,var(--green-light),var(--green-dark));color:var(--white);text-align:center;line-height:54px;font-size:22px;font-weight:900;text-transform:uppercase}

/* broker */
.broker{left:74px;top:2124px;width:1052px;height:84px;background:var(--orange);display:flex;align-items:center}
.broker-photo{width:146px;height:84px;background:linear-gradient(180deg,#5f6f86,#2c3a52)}
.broker-title{margin-left:22px;font-family:'Oswald',Arial,sans-serif;font-weight:500;font-size:34px;color:var(--white);text-transform:uppercase;letter-spacing:.5px}
.broker-btn{position:absolute;right:36px;top:16px;width:170px;height:52px;background:var(--yellow);border-radius:5px;display:flex;align-items:center;justify-content:center;gap:10px;font-family:'Oswald',Arial,sans-serif;font-weight:500;font-size:24px;color:var(--black);text-transform:uppercase}

/* footer */
.footer-top-line{left:0;top:2246px;width:1200px;height:6px;background:#4a4a4a}
.site-footer{left:0;top:2252px;width:1200px;height:316px;background:var(--black)}
.footer-col h4{font-size:15px;font-weight:900;color:var(--white);text-transform:uppercase}
.footer-col p,.footer-col li{font-size:13px;line-height:20px;color:var(--footer-text);list-style:none}
.footer-col .body{margin-top:14px}
.col-contact{left:74px;top:46px;width:300px}
.col-links{left:624px;top:46px}
.col-main{left:796px;top:46px}
.col-wv{left:970px;top:46px}
.badges{left:74px;top:172px;display:flex;gap:8px}
.badges span{display:block;height:38px;background:#d6d6d6}
.footer-brand{left:90px;top:232px;display:flex;align-items:center;gap:10px}
.footer-brand .brand-dot{width:46px;height:46px}
.footer-brand .brand-name{font-size:26px;color:var(--white)}
.footer-phones{left:318px;top:256px;font-size:15px;color:#999}
.footer-social{left:1018px;top:250px}
.footer-social span{width:32px;height:32px}
.copyright{left:0;top:2568px;width:1200px;height:41px;background:#2a2a2a;text-align:center;line-height:41px;font-size:12px;color:#777}
</style>
</head>
<body>

<header class="site-header abs">
  <div class="brand abs"><span class="brand-dot"></span><span class="brand-name">Stoneridge</span></div>
  <div class="social header-social abs"><span></span><span></span><span></span></div>
  <svg class="phone-icon abs" width="34" height="34" viewBox="0 0 24 24"><path fill="#111" d="M6.6 10.8c1.4 2.8 3.8 5.1 6.6 6.6l2.2-2.2c.3-.3.7-.4 1-.2 1.1.4 2.3.6 3.6.6.6 0 1 .4 1 1V20c0 .6-.4 1-1 1C10.6 21 3 13.4 3 4c0-.6.4-1 1-1h3.5c.6 0 1 .4 1 1 0 1.3.2 2.5.6 3.6.1.3 0 .7-.2 1z"/></svg>
  <div class="office-contact contact-va abs"><div class="label">Marston, VA:</div><div class="phone">(800) 555-0173</div></div>
  <div class="header-divider abs"></div>
  <div class="office-contact contact-wv abs"><div class="label">Dunmore, WV:</div><div class="phone">(304) 555-0192</div></div>
</header>

<nav class="main-nav abs">
  <ul>
    <li class="active">Home</li>
    <li>Auction Calendar</li>
    <li>Real Estate Listings</li>
    <li>About</li>
    <li>FAQs &amp; Terms</li>
    <li>Contact</li>
  </ul>
</nav>

<section class="hero abs" role="img" aria-label="Slideshow photo of a green valley with rolling hills and farmland framed by trees"></section>
<svg class="hero-arrow arrow-left abs" width="28" height="48" viewBox="0 0 28 48"><path d="M24 4 6 24l18 20" fill="none" stroke="#fff" stroke-width="3"/></svg>
<svg class="hero-arrow arrow-right abs" width="28" height="48" viewBox="0 0 28 48"><path d="M4 4l18 20L4 44" fill="none" stroke="#fff" stroke-width="3"/></svg>

<section class="welcome abs">
  <h1 class="section-title">Welcome to Stoneridge Real Estate &amp; Auction</h1>
  <p>Stoneridge's Real Estate &amp; Auction Company has been in business for over 60 years. Stoneridge's was started in Marston Virginia by Walter Stoneridge. My father purchased Stoneridge's from Walter in 1960. I worked with my father, Henry, as partners until his death in 1986. I took over the business as the Owner, Broker, and Auctioneer for Stoneridge's Real Estate &amp; Auction Company.Today the Auction Company is one of the fastest growing full service auction companies in the area with 2 locations: Marston, Virginia, and Dunmore, West Virginia. Stoneridge's does over 20 million in yearly sales and completes approximately fifty Personal Property and/or Real Estate auctions a year throughout the mid Atlantic states.</p>
</section>

<section class="auctions abs">
  <h2 class="section-title">Upcoming Auctions</h2>
  <article class="auction-card abs" style="left:80px">
    <div class="flyer"><div class="flyer-bw" role="img" aria-label="Auction flyer for two lots with a plat map"></div></div>
    <h3>2 Lots for Sale in Hollis County, VA</h3>
    <p>05/09/15 at 11:00 AM EDT<br>211 Fern Drive<br>Marston, VA 24873</p>
    <span class="btn-details">DETAILS</span>
  </article>
  <article class="auction-card abs" style="left:348px">
    <div class="flyer"><div class="flyer-green" role="img" aria-label="Auction flyer with photos of a home on 12 acres"></div></div>
    <h3>3400 Sq. Ft. Home on 12 Acres +/-</h3>
    <p>05/16/15 at 11:00 AM EDT<br>45 Laurel Creek Turnpike<br>Ashby Springs, VA 24861</p>
    <span class="btn-details">DETAILS</span>
  </article>
  <article class="auction-card abs" style="left:616px">
    <div class="flyer"><div class="flyer-red" role="img" aria-label="Auction flyer for building lots"></div></div>
    <h3>22 Building Lots AT AUCTION</h3>
    <p>05/23/15 at 11:00 AM EDT<br>520 Thistle Lane<br>Marston, VA 24873</p>
    <span class="btn-details">DETAILS</span>
  </article>
  <article class="auction-card abs" style="left:884px">
    <div class="flyer"><div class="flyer-bw" role="img" aria-label="Auction flyer for building lots with a plat map"></div></div>
    <h3>Ideal Building Lots with Panoramic Views</h3>
    <p>05/09/15 at 11:00 AM EDT<br>211 Fern Drive<br>Marston, VA 24873</p>
    <span class="btn-details">DETAILS</span>
  </article>
</section>

<section class="testimonials abs">
  <h2 class="section-title">What Our Clients Say</h2>
  <svg class="quote-mark" width="52" height="52" viewBox="0 0 52 52"><circle cx="26" cy="26" r="26" fill="#9bbd1e"/><path d="M15 31v-7c0-4 2-7 6-8l1 2c-2 1-3 3-3 5h3v8zm13 0v-7c0-4 2-7 6-8l1 2c-2 1-3 3-3 5h3v8z" fill="#fff"/></svg>
  <blockquote>"Lorem ipsum dolor sit amet, consectetur adipiscing elit, sed do eiusmod tempor incididunt ut labore et dolore magna aliqua. Ut enim ad minim veniam, quis nostrud exercitation ullamco laboris nisi ut aliquip ex ea commodo consequat."</blockquote>
  <div class="client">
    <div class="client-photo" role="img" aria-label="Client portrait"></div>
    <div class="client-meta"><strong>Dana Whitlock</strong><span>Lorem ipsum dolor</span></div>
  </div>
  <div class="dots"><span class="on"></span><span></span><span></span><span></span></div>
</section>

<section class="alerts abs">
  <h2>Auction Alerts!</h2>
  <p>Sign up to receive email alerts about our upcoming auctions</p>
  <form><div class="field">Enter your email address</div><div class="subscribe">Subscribe</div></form>
</section>

<section class="question abs">
  <h2>Do you have a question?</h2>
  <div class="rule"></div>
  <label>Your Name*</label>
  <div class="pair"><div class="input">First Name</div><div class="input">Last Name</div></div>
  <label>Email*</label>
  <div class="input">Your Email Address here</div>
  <label>Phone</label>
  <div class="input">Phone Number</div>
  <label>Comments*</label>
  <div class="textarea"></div>
  <div class="submit">Submit</div>
</section>

<section class="broker abs">
  <div class="broker-photo" role="img" aria-label="Photo of a broker in a suit"></div>
  <div class="broker-title">Broker Participation Form</div>
  <div class="broker-btn">Click here
    <svg width="24" height="24" viewBox="0 0 24 24"><circle cx="12" cy="12" r="10" fill="none" stroke="#111" stroke-width="2"/><path d="M10 7l5 5-5 5" fill="none" stroke="#111" stroke-width="2"/></svg>
  </div>
</section>

<div class="footer-top-line abs"></div>
<footer class="site-footer abs">
  <div class="footer-col col-contact abs">
    <h4>Contact Us Today!</h4>
    <p class="body">Stoneridge's is a full service auction firm, which means we are equipped to provide everything needed to make your auction experience a pleasurable one.</p>
  </div>
  <div class="footer-col col-links abs">
    <h4>Links</h4>
    <ul class="body"><li>Home</li><li>Auction Calendar</li><li>Real Estate Listings</li><li>About</li><li>FAQs &amp; Terms</li><li>Contact</li></ul>
  </div>
  <div class="footer-col col-main abs">
    <h4>Main Office</h4>
    <p class="body">417 E Hazel Rd<br>Marston, VA 24873<br>(800) 555-0173<br>(540) 555-0148</p>
  </div>
  <div class="footer-col col-wv abs">
    <h4>Dunmore Office</h4>
    <p class="body">318 1/2 S. Mill Rd.<br>Dunmore, WV 24987<br>(304) 555-0192</p>
  </div>
  <div class="badges abs"><span style="width:38px"></span><span style="width:30px"></span><span style="width:30px"></span><span style="width:70px"></span><span style="width:70px"></span><span style="width:80px"></span></div>
  <div class="footer-brand abs"><span class="brand-dot"></span><span class="brand-name">Stoneridge</span></div>
  <div class="footer-phones abs">Marston, VA: (800) 555-0173 &nbsp;|&nbsp; Dunmore, WV: (304) 555-0192</div>
  <div class="social footer-social abs"><span></span><span></span><span></span></div>
</footer>
<div class="copyright abs">© 2015 • Stoneridge Real Estate &amp; Auction All Rights Reserved.</div>

</body>
</html>
```